Bertrand Music Video and Film Production

THE FLYER SHOULD INCLUDE THIS TEXT:

"PROFESSIONAL FILM AND MUSIC VIDEO DIRECTzOR WITH OVER 10 YEARS EXPERIENCE. CLIENT LIST INCLUDES, 714, MARWICK, PALE HARBOURS, BRAMBLEGATE, THE LANTERNS, BLUE OAK, TAMSIN-JO, NELL MARIS, QRV, WILLOWTREE.
HD, SUPER 8, LIVE DVD, PROMO REELS AND VIDEOS ON TIME AND ON BUDGET."

I need to create a flyer/ad that I will use to promote myself and the services I provide.

My name is Bertrand Vellacott and I am a music video clip director and editor that can achieve great results regardless of budgets.

Working with HD and Super 8 vintage film formats to achieve the look you want.

I am a Melbourne based film maker with a huge client list; 714, Marwick, Pale Harbours, Nell Maris, Tamsin-Jo, Bramblegate, The Lanterns, Dominic Plaskett, Willowtree Marketing, QRV and Carrowvale Shire Council.

Black and white classic design. Clean and neat not too busy, almost minimal in a way. Incorpirate my initials to create a logo perhaps.

It needs to appeal and relate to various music genres including; rock, pop, soul, funk, country and folk as I make music videos for artists of many genres.

Feature my website:

www.clipvaultia.com/bertvella

Include my email address

bertrandvellacott@mailzephra.com

Many thanks

Bertrand

Target Market(s)

Music artists and bands performing all sorts of music styles from; rock, soul, funk, pop, country and folk.

Appealing also to band managers, artist representation and record labels/music publishers.

Industry/Entity Type

Artists

Requirements
Must have
• My website and email address and my name. I am a sole trader so i don't have a business name as such, just my name, Bertrand Vellacott.
Should not have
• a picture of me

```html
<!DOCTYPE html>
<html lang="en">
<head>
<meta charset="utf-8">
<title>Bertrand Vellacott – Film and Music Video Production</title>
<link rel="stylesheet" href="https://fonts.googleapis.com/css2?family=Alfa+Slab+One&family=Share+Tech&family=Raleway:wght@300;400&family=Open+Sans:wght@400&display=swap">
<style>
  :root {
    --bg-dark: #1c1e1f;
    --bg-mid: #2e3233;
    --title-green: #e2efcf;
    --bubble-fill: #d9e9c0;
    --bubble-edge: #eef6e2;
    --body-ink: #262a24;
    --name-white: #f4f4f0;
    --bar-green: #7fae3c;
    --bar-text: #ffffff;
  }
  html, body {
    margin: 0;
    padding: 0;
    overflow: hidden;
    background: var(--bg-dark);
  }
  .flyer {
    position: relative;
    width: 847px;
    height: 1200px;
    overflow: hidden;
    background:
      radial-gradient(ellipse at 45% 40%, var(--bg-mid) 0%, var(--bg-dark) 75%);
  }
  .splash-art {
    position: absolute;
    right: 0;
    top: 0;
    width: 320px;
    height: 320px;
    background:
      radial-gradient(circle at 60% 45%, rgba(240,240,255,0.55) 0%, rgba(130,170,255,0.35) 25%, rgba(220,90,200,0.25) 45%, rgba(28,30,31,0) 70%);
  }
  .music-art {
    position: absolute;
    left: 0;
    bottom: 0;
    width: 480px;
    height: 280px;
    background:
      radial-gradient(ellipse at 30% 60%, rgba(90,96,92,0.45) 0%, rgba(60,64,62,0.25) 40%, rgba(28,30,31,0) 72%);
  }
  .headline {
    position: absolute;
    left: 60px;
    top: 30px;
    margin: 0;
    font-family: "Alfa Slab One", "Rockwell", serif;
    font-weight: 400;
    font-size: 86px;
    line-height: 98px;
    letter-spacing: 2px;
    color: var(--title-green);
    text-transform: uppercase;
  }
  .bubble-shape {
    position: absolute;
    left: 0;
    top: 0;
  }
  .bubble-text {
    position: absolute;
    left: 155px;
    top: 370px;
    width: 598px;
    margin: 0;
    font-family: "Share Tech", "Arial Narrow", sans-serif;
    font-size: 28px;
    line-height: 41px;
    letter-spacing: 1px;
    color: var(--body-ink);
    text-transform: uppercase;
    text-align: justify;
    hyphens: auto;
  }
  .signature {
    position: absolute;
    right: 30px;
    top: 905px;
    text-align: right;
    color: var(--name-white);
    font-family: "Raleway", "Helvetica Neue", sans-serif;
    text-transform: uppercase;
  }
  .signature .first-name {
    display: block;
    font-weight: 300;
    font-size: 46px;
    letter-spacing: 3px;
    line-height: 50px;
  }
  .signature .last-name {
    display: block;
    font-weight: 400;
    font-size: 64px;
    letter-spacing: 2px;
    line-height: 70px;
  }
  .contact-bar {
    position: absolute;
    right: 0;
    height: 30px;
    padding: 0 14px 0 16px;
    background: var(--bar-green);
    color: var(--bar-text);
    font-family: "Open Sans", "Arial", sans-serif;
    font-size: 18px;
    line-height: 30px;
    white-space: nowrap;
  }
  .contact-web { top: 1047px; }
  .contact-email { top: 1098px; }
</style>
</head>
<body>
  <main class="flyer">
    <div class="splash-art" role="img" aria-label="Colourful smoke and light splash decoration"></div>
    <div class="music-art" role="img" aria-label="Faint script lettering and music notes decoration"></div>

    <h1 class="headline">Film and<br>Music Video<br>Production</h1>

    <svg class="bubble-shape" width="847" height="1200" viewBox="0 0 847 1200" aria-hidden="true">
      <path d="M127 339 H777 V904 H240 L170 975 L185 904 H127 Z"
            fill="var(--bubble-fill)" stroke="var(--bubble-edge)" stroke-width="4"/>
    </svg>

    <p class="bubble-text" lang="en">Professional film and music video director with over 10 years experience. Client list includes, 714, Marwick, Pale Harbours, Bramblegate, The Lanterns, Blue Oak, Tamsin-Jo, Nell Maris, QRV, Willowtree. HD, Super 8, live DVD, promo reels and videos on time and on budget.</p>

    <div class="signature">
      <span class="first-name">Bertrand</span>
      <span class="last-name">Vellacott</span>
    </div>

    <div class="contact-bar contact-web">web: www.clipvaultia.com/bertvella</div>
    <div class="contact-bar contact-email">email:bertrandvellacott@mailzephra.com</div>
  </main>
</body>
</html>
```